Packaging for new Hair Product

Need packaging for a product. These are packets of "wipes" like you would see for hands or face use, but these are for Hair! These wipes are to tame your fly-aways and static on the go. I would like a graphic of flowing hair on the package . Since its just two colors, I think a graphic and not a real photo might work best. The name of the product is Strand Soothers - you can be creative with the font, as I don;t really have a logo (or I can pay extra if you want to make a true logo) . Info needed on package: Name: Strand Soothers.
Great hair on the Go.
Tame your fly-aways and static with a wipe.
Contains Coconut oil, witch hazel and aloe

Ingredients:
Diazolidiny1 Urea
Phenoxyethanol
Polysorbate 20
Glycerin
Propylene Glycol
Cetearyl Isononanoate
Ceteareth -20
Coconut Oil
Glyceryl Stearate
Cetearyl Alcohol
Cetyl Palmitate
Aloe Barbadensis extract
Chamomile Recutita Extract
Witch Hazel
Citric Acid
Water

KOR, LLC products
Made in China
UPC attached

Target Market(s)

woman 20-50

Requirements
Must have
• Use the attached die and cut
• 2 color graphics only. Plus the information listed:
• UPC
• Info needed on package: Name: Strand Soothers.
• Great hair on the Go.
• Tame your fly-aways and static with a wipe.
• Contains Coconut oil, witch hazel and aloe
• Ingredients:
• Diazolidiny1 Urea
• Phenoxyethanol
• Polysorbate 20
• Glycerin
• Propylene Glycol
• Cetearyl Isononanoate
• Ceteareth -20
• Coconut Oil
• Glyceryl Stearate
• Cetearyl Alcohol
• Cetyl Palmitate
• Aloe Barbadensis extract
• Chamomile Recutita Extract
• Witch Hazel
• Citric Acid
• Water
• KOR, LLC products
• Made in China
• UPC attached

```html
<!DOCTYPE html>
<html lang="en">
<head>
<meta charset="utf-8">
<title>Strand Soothers – Hair Wipes Packet</title>
<link rel="stylesheet" href="https://fonts.googleapis.com/css2?family=Montserrat:wght@700&family=Lato:wght@400&display=swap">
<style>
  :root {
    --backdrop: #e4e6e9;
    --ink: #1f1f22;
    --pack-blue: #1c9fd6;
    --pack-blue-deep: #1585bd;
    --pack-white: #f7f8f9;
    --lid-white: #eef0f2;
    --mark-blue: #2f7fbf;
    --crimp-line: #d4d8dc;
    --crimp-line-blue: #137fb4;
  }
  html, body {
    margin: 0;
    padding: 0;
    overflow: hidden;
  }
  body {
    width: 1200px;
    height: 950px;
    background: var(--backdrop);
    position: relative;
  }
  .brand-heading {
    position: absolute;
    top: 140px;
    left: 0;
    width: 1200px;
    display: flex;
    justify-content: center;
    align-items: center;
    gap: 14px;
    font-family: "Montserrat", sans-serif;
    font-weight: 700;
    font-size: 36px;
    letter-spacing: 1px;
    color: var(--ink);
    text-transform: uppercase;
  }
  .brand-heading .brand-dot {
    width: 26px;
    height: 26px;
    border-radius: 50%;
    background: var(--mark-blue);
  }
  .wipes-packet {
    position: absolute;
    left: 150px;
    top: 284px;
    width: 908px;
    height: 504px;
  }
  .wipes-packet svg { display: block; }
  .pack-brand {
    font-family: "Montserrat", sans-serif;
    font-weight: 700;
    font-size: 30px;
    fill: var(--ink);
    letter-spacing: 0.5px;
  }
  .lid-brand {
    font-family: "Montserrat", sans-serif;
    font-weight: 700;
    font-size: 26px;
    fill: var(--ink);
  }
  .claim-copy {
    font-family: "Lato", sans-serif;
    font-size: 16.5px;
    fill: #ffffff;
  }
  .tagline {
    font-family: "Lato", sans-serif;
    font-size: 25px;
    fill: var(--ink);
  }
</style>
</head>
<body>

<div class="brand-heading">
  <span class="brand-name">Strand Soothers</span>
  <span class="brand-dot"></span>
</div>

<div class="wipes-packet">
  <svg width="908" height="504" viewBox="0 0 908 504" xmlns="http://www.w3.org/2000/svg">
    <defs>
      <clipPath id="pack-shape">
        <rect x="0" y="0" width="908" height="504" rx="4"/>
      </clipPath>
      <linearGradient id="botanical-tone" x1="0" y1="0" x2="1" y2="1">
        <stop offset="0" stop-color="#3cb2e2" stop-opacity="0.35"/>
        <stop offset="1" stop-color="#1c9fd6" stop-opacity="0"/>
      </linearGradient>
    </defs>

    <g clip-path="url(#pack-shape)">
      <!-- blue body -->
      <rect class="pack-body" x="0" y="0" width="908" height="504" fill="var(--pack-blue)"/>

      <!-- botanical line drawings area -->
      <rect class="botanical-pattern" x="240" y="0" width="668" height="504" fill="url(#botanical-tone)"
            role="img" aria-label="Faint line drawings of coconuts, aloe leaves and witch hazel blossoms"/>

      <!-- white side panel with wave edge -->
      <path class="side-panel" d="M0,0 L232,0 C252,70 300,130 272,250 C248,360 152,430 132,504 L0,504 Z" fill="var(--pack-white)"/>

      <!-- wave stripes -->
      <path class="wave-line-blue" d="M238,0 C258,70 306,130 278,250 C254,360 158,430 138,504" fill="none" stroke="var(--pack-blue-deep)" stroke-width="3"/>
      <path class="wave-band-black" d="M258,0 C278,70 324,132 296,252 C272,362 176,432 156,504" fill="none" stroke="var(--ink)" stroke-width="10"/>

      <!-- crimped seals -->
      <g class="seal-left" stroke="var(--crimp-line)" stroke-width="1.5">
        <line x1="8" y1="0" x2="8" y2="504"/>
        <line x1="16" y1="0" x2="16" y2="504"/>
        <line x1="24" y1="0" x2="24" y2="504"/>
        <line x1="32" y1="0" x2="32" y2="504"/>
        <line x1="40" y1="0" x2="40" y2="504"/>
        <line x1="48" y1="0" x2="48" y2="504"/>
      </g>
      <g class="seal-right" stroke="var(--crimp-line-blue)" stroke-width="1.5">
        <line x1="860" y1="0" x2="860" y2="504"/>
        <line x1="868" y1="0" x2="868" y2="504"/>
        <line x1="876" y1="0" x2="876" y2="504"/>
        <line x1="884" y1="0" x2="884" y2="504"/>
        <line x1="892" y1="0" x2="892" y2="504"/>
        <line x1="900" y1="0" x2="900" y2="504"/>
      </g>
    </g>

    <!-- vertical brand name -->
    <text class="pack-brand" transform="translate(122,254) rotate(-90)" text-anchor="middle">STRAND SOOTHERS</text>

    <!-- resealable lid -->
    <path class="lid" d="M298,150 Q298,130 318,130 L610,130 Q630,130 630,150 L630,308 Q630,318 620,320 L545,322 Q505,326 470,352 Q440,370 412,352 Q380,326 340,322 L308,320 Q298,318 298,308 Z"
          fill="var(--lid-white)" stroke="#d9dde1" stroke-width="1.5"/>
    <circle class="lid-dot" cx="464" cy="192" r="18" fill="var(--mark-blue)"/>
    <text class="lid-brand" x="464" y="260" text-anchor="middle">Strand Soothers</text>

    <!-- claims -->
    <text class="claim-copy" x="304" y="444">Tame your fly-aways and static with a wipe.</text>
    <text class="claim-copy" x="304" y="467">Contains Coconut oil, witch hazel and aloe</text>

    <!-- tagline pill -->
    <rect class="tagline-pill" x="740" y="102" width="56" height="300" rx="28" fill="var(--lid-white)"/>
    <text class="tagline" transform="translate(777,252) rotate(-90)" text-anchor="middle">Great Hair on the Go.</text>
  </svg>
</div>

</body>
</html>
```